Business Card for a Floral & Decorating Business

I would like to take my current logo and create a better business card. I am looking for elegance as I am a florist and event decorator. My logo has multiple colour options. I like colours like green, purple, pink and orange, I think I would like a white card, open to black back ground. I want it to feel elegant and romantic. I like metallic lettering that maybe is indented in the paper, I also like glossy paper. I have a full logo already as well as a badge. I have attached both in multiple colours.m
Updates

Need extra days to review

Target Market(s)

Weddings, special events, floral customers

Industry/Entity Type

Floral and decorating

Contact Information for Business Card

Phone number, email, instagram, facebook, title, name, logo

Font styles to use
Script

Requirements
Nice to have
• Elegant

```html
<!DOCTYPE html>
<html lang="en">
<head>
<meta charset="utf-8">
<title>Marlowe Ashby — Business Card</title>
<link rel="stylesheet" href="https://fonts.googleapis.com/css2?family=Allura&family=Cormorant+Garamond:wght@500&family=Arimo:wght@400;700&display=swap">
<style>
  :root {
    --backdrop: #ababab;
    --card-white: #ffffff;
    --berry: #9c455e;
    --berry-soft: #e8c9d2;
    --berry-deep: #b8687f;
    --contact-grey: #a3a3a3;
    --floral-grey-light: #f3f3f3;
    --floral-grey: #e3e3e3;
  }
  * { margin: 0; padding: 0; box-sizing: border-box; }
  html, body {
    width: 1200px; height: 1000px; overflow: hidden;
    background: var(--backdrop);
  }
  .canvas { position: relative; width: 1200px; height: 1000px; }
  .card {
    position: absolute; left: 293px; width: 615px; height: 355px;
    overflow: hidden; text-align: center;
  }
  .card--front { top: 112px; background: var(--card-white); }
  .card--back { top: 564px; background: var(--berry); }

  .floral-panel {
    position: absolute; top: 0; width: 148px; height: 100%;
  }
  .floral-panel--left {
    left: 0;
    background: linear-gradient(90deg, var(--floral-grey) 0%, var(--floral-grey-light) 70%, var(--card-white) 100%);
  }
  .floral-panel--right {
    right: 0;
    background: linear-gradient(270deg, var(--floral-grey) 0%, var(--floral-grey-light) 70%, var(--card-white) 100%);
  }

  .monogram {
    position: absolute; border-radius: 4px;
  }
  .card--front .monogram {
    left: 280px; top: 33px; width: 59px; height: 77px;
    background: linear-gradient(180deg, var(--berry-soft), #f4e3e8);
  }
  .card--back .monogram {
    left: 274px; top: 63px; width: 83px; height: 113px;
    background: linear-gradient(180deg, var(--berry-deep), #a9546c);
  }

  .brand-name {
    position: absolute; left: 0; right: 0;
    font-family: "Allura", cursive;
    font-weight: 400;
    line-height: 1;
    white-space: nowrap;
  }
  .brand-tagline {
    position: absolute; left: 0; right: 0;
    font-family: "Cormorant Garamond", serif;
    font-weight: 500;
    text-transform: uppercase;
    white-space: nowrap;
  }
  .card--front .brand-name { top: 110px; font-size: 54px; letter-spacing: 4px; color: var(--berry); }
  .card--front .brand-tagline { top: 166px; font-size: 10px; letter-spacing: 3px; color: var(--berry); }
  .card--back .brand-name { top: 170px; font-size: 80px; letter-spacing: 6px; color: var(--card-white); }
  .card--back .brand-tagline { top: 254px; font-size: 14px; letter-spacing: 4.6px; color: var(--card-white); }

  .contact {
    position: absolute; left: 0; right: 0; top: 202px;
    font-family: "Arimo", Arial, sans-serif; color: var(--contact-grey);
  }
  .contact__phone { font-size: 18px; font-weight: 700; line-height: 22px; }
  .contact__email { font-size: 18px; line-height: 24px; }
  .social { margin-top: 26px; font-size: 15px; line-height: 24px; }
  .social__item { display: flex; justify-content: center; align-items: center; gap: 5px; }
  .social__dot {
    width: 14px; height: 14px; flex: none; border-radius: 50%;
    background: var(--contact-grey);
  }
</style>
</head>
<body>
<main class="canvas">
  <section class="card card--front" aria-label="Card front">
    <div class="floral-panel floral-panel--left" role="img" aria-label="Light grey line-drawn flowers and leaves along the left edge"></div>
    <div class="floral-panel floral-panel--right" role="img" aria-label="Light grey line-drawn flowers and leaves along the right edge"></div>
    <div class="monogram" role="img" aria-label="Floral monogram letter mark in berry"></div>
    <h1 class="brand-name">marlowe ashby</h1>
    <p class="brand-tagline">Decorating &amp; Florals.</p>
    <div class="contact">
      <p class="contact__phone">(555) 318-0426</p>
      <p class="contact__email">marloweashby@example.com</p>
      <div class="social">
        <p class="social__item"><span class="social__dot" aria-hidden="true"></span>marloweashbydecorating.florals</p>
        <p class="social__item"><span class="social__dot" aria-hidden="true"></span>everafterdecorating</p>
      </div>
    </div>
  </section>

  <section class="card card--back" aria-label="Card back">
    <div class="monogram" role="img" aria-label="Floral monogram letter mark in white"></div>
    <h2 class="brand-name">marlowe ashby</h2>
    <p class="brand-tagline">Decorating &amp; Florals.</p>
  </section>
</main>
</body>
</html>
```